EPS Packaging Infographic

We need two infographics focus on EPS packaging.

I've attached the copy as well as some of our other infographics to give you an idea of our style.

```html
<!DOCTYPE html>
<html lang="en">
<head>
<meta charset="utf-8">
<title>Make the Right Choice for the Environment</title>
<link href="https://fonts.googleapis.com/css2?family=Bebas+Neue&family=Open+Sans:wght@400&display=swap" rel="stylesheet">
<style>
  :root {
    --brown: #5b2e20;
    --blue: #578aa1;
    --orange: #f4a323;
    --olive: #9b9737;
    --yellow: #f0cf12;
    --label: #575757;
    --divider: #a3a3a3;
    --paper: #ffffff;
  }
  html, body {
    margin: 0;
    padding: 0;
    background: var(--paper);
    overflow: hidden;
  }
  .infographic {
    display: block;
    width: 849px;
    height: 1200px;
  }
  .headline { font-family: 'Bebas Neue', Impact, sans-serif; }
  .headline-dark { fill: var(--brown); }
  .headline-blue { fill: var(--blue); }
  .headline-orange { fill: var(--orange); }
  .subhead { font-family: 'Bebas Neue', Impact, sans-serif; fill: var(--blue); }
  .slice { stroke: var(--divider); stroke-width: 3; stroke-linejoin: round; }
  .slice-dropoff { fill: var(--orange); }
  .slice-bans { fill: var(--brown); }
  .slice-curbside { fill: var(--olive); }
  .slice-events { fill: var(--blue); }
  .slice-mail { fill: var(--yellow); }
  .hub-ring { fill: var(--paper); stroke: #dcdcdc; stroke-width: 1; }
  .hub-core { fill: var(--olive); }
  .hub-icon { fill: none; stroke: var(--paper); stroke-width: 9; stroke-linecap: butt; }
  .hub-arrowhead { fill: var(--paper); }
  .leader { fill: none; stroke: #4a4a4a; stroke-width: 1.3; }
  .label { font-family: 'Bebas Neue', Impact, sans-serif; font-size: 24px; fill: var(--label); }
  .source { font-family: 'Open Sans', Arial, sans-serif; font-size: 12px; fill: #666; }
  .brand-name { font-family: 'Bebas Neue', Impact, sans-serif; font-size: 22px; fill: var(--label); }
</style>
</head>
<body>
<svg class="infographic" viewBox="0 0 849 1200" xmlns="http://www.w3.org/2000/svg" role="img" aria-label="Expanded polystyrene number 6 recycling infographic">
  <text class="headline headline-dark" x="55" y="120" font-size="104" textLength="730" lengthAdjust="spacingAndGlyphs">MAKE THE RIGHT CHOICE</text>
  <text class="headline headline-blue" x="55" y="201" font-size="104" textLength="108" lengthAdjust="spacingAndGlyphs">FOR</text>
  <text class="headline headline-orange" x="55" y="307" font-size="127" textLength="731" lengthAdjust="spacingAndGlyphs">THE ENVIRONMENT</text>

  <text class="subhead" x="66" y="416" font-size="57" textLength="725" lengthAdjust="spacingAndGlyphs">EXPANDED POLYSTYRENE (EPS) #6 RECYCLING</text>

  <g class="pie-chart">
    <path class="slice slice-dropoff" d="M437 762 L170.7 732.1 A268 268 0 0 1 705 762 Z"/>
    <path class="slice slice-bans" d="M437 762 L705 762 A268 268 0 0 1 434.7 1030 Z"/>
    <path class="slice slice-curbside" d="M437 762 L434.7 1030 A268 268 0 0 1 225.8 927.1 Z"/>
    <path class="slice slice-events" d="M437 762 L225.8 927.1 A268 268 0 0 1 169.2 772.3 Z"/>
    <path class="slice slice-mail" d="M437 762 L169.2 772.3 A268 268 0 0 1 170.7 732.1 Z"/>

    <circle class="hub-ring" cx="437" cy="762" r="79"/>
    <circle class="hub-core" cx="437" cy="762" r="66"/>
    <g class="hub-icon-group">
      <path class="hub-icon" d="M410 754 A30 30 0 0 1 452 736"/>
      <path class="hub-icon" d="M464 760 A30 30 0 0 1 436 794"/>
      <path class="hub-icon" d="M420 790 A30 30 0 0 1 407 768"/>
      <polygon class="hub-arrowhead" points="448,724 466,744 443,748"/>
      <polygon class="hub-arrowhead" points="446,784 430,806 425,784"/>
      <polygon class="hub-arrowhead" points="397,772 408,748 419,770"/>
    </g>
  </g>

  <polyline class="leader" points="551,542 598,499 629,499"/>
  <polyline class="leader" points="190,758 108,752 82,714"/>
  <polyline class="leader" points="218,851 136,864 112,904"/>
  <polyline class="leader" points="315,987 271,1043"/>
  <polyline class="leader" points="606,944 675,980"/>

  <text class="label" x="643" y="508">DROP OFF LOCATIONS, 280</text>
  <text class="label" x="19" y="673">NATIONAL MAIL BACK</text>
  <text class="label" x="19" y="700">LOCATIONS, 20</text>
  <text class="label" x="24" y="934">SPECIAL COLLECTION</text>
  <text class="label" x="24" y="962">EVENTS/YEAR, 50+</text>
  <text class="label" x="93" y="1069">CURBSIDE PROGRAMS, 82</text>
  <text class="label" x="682" y="993">LOCAL BANS, 146</text>

  <text class="source" x="49" y="1183">Source: https://www.recyclingdigest.org/plastics/2016/12/08/rise-foam-ordinances/</text>
  <text class="brand-name" x="806" y="1163" text-anchor="end">FOAM PACK COUNCIL</text>
</svg>
</body>
</html>
```